Nat Account Banner Stand 91H x 31.5"

create Poster for Retractable Banner Stand (91" High x 31.5"W).

Images Provided via Dropbox link
https://www.filquorra.com/sh/pmwq8vtrkzhe4/BBFmRz7kPqXs2Lw9YtUvHKNe?dl=0

Concept should come from this "look" http://storage.velmaprint.com/design_img/738205/94126/94126_5817042_738205_image.jpg

```html
<!DOCTYPE html>
<html lang="en">
<head>
<meta charset="utf-8">
<title>KVR National Accounts – Banner Stand</title>
<link href="https://fonts.googleapis.com/css2?family=Questrial&display=swap" rel="stylesheet">
<style>
  :root{
    --paper:#ffffff;
    --header-top:#ffffff;
    --header-bottom:#ecebf2;
    --brand-red:#c3262c;
    --brand-grey:#8e8e92;
    --text:#55555c;
    --lavender-light:#e6e5ee;
    --gap:#ffffff;
  }
  *{margin:0;padding:0;box-sizing:border-box}
  html,body{width:1200px;height:1000px;overflow:hidden;background:var(--paper)}
  body{position:relative;font-family:"Questrial",sans-serif;color:var(--text)}
  .banner{position:absolute;top:0;width:348px;height:1000px}
  .banner--one{left:26px}
  .banner--two{left:426px}
  .banner--three{left:824px}

  .banner__header{position:absolute;top:0;left:0;width:348px;height:140px;
    background:linear-gradient(var(--header-top),var(--header-bottom))}
  .brand{position:absolute;left:29px;top:27px;display:flex;align-items:flex-start;gap:12px}
  .brand__square{width:94px;height:94px;background:var(--brand-red)}
  .brand__name{font-size:80px;line-height:64px;color:var(--brand-grey);letter-spacing:3px;margin-top:2px}
  .brand__division{position:absolute;left:136px;top:93px;width:190px;display:flex;align-items:center;gap:6px;
    font-size:12px;color:var(--brand-grey);letter-spacing:.4px;white-space:nowrap}
  .brand__division::before,.brand__division::after{content:"";flex:1;height:1px;background:var(--brand-grey)}
  .brand__tagline{position:absolute;left:136px;top:108px;font-size:12.5px;color:var(--brand-red);letter-spacing:.3px;white-space:nowrap}

  .banner__art{position:absolute;top:152px;left:0;width:348px;height:848px}

  .offer{position:absolute;left:14px;top:625px;width:236px}
  .offer__title{font-size:12px;line-height:14px;margin-bottom:5px}
  .offer__list{list-style:none;font-size:10.3px;line-height:12px}

  .contact{position:absolute;left:17px;top:730px;list-style:none}
  .contact__item{display:flex;align-items:center;gap:12px;height:31px;font-size:16px}
  .contact__icon{width:24px;height:20px}
</style>
</head>
<body>

<section class="banner banner--one">
  <header class="banner__header">
    <div class="brand"><span class="brand__square"></span><span class="brand__name">KVR</span></div>
    <div class="brand__division">NATIONAL ACCOUNTS</div>
    <div class="brand__tagline">PARTNERSHIP AT EVERY LEVEL</div>
  </header>
  <svg class="banner__art" viewBox="0 0 348 848">
    <defs>
      <linearGradient id="atrium1" x1="0" y1="0" x2="1" y2="1"><stop offset="0" stop-color="#f5eddd"/><stop offset=".3" stop-color="#ecdcbb"/><stop offset=".5" stop-color="#c9b792"/><stop offset=".65" stop-color="#717756"/><stop offset=".85" stop-color="#4e4a37"/><stop offset="1" stop-color="#3a3226"/></linearGradient>
      <linearGradient id="store1" x1="0" y1="0" x2="1" y2="1"><stop offset="0" stop-color="#a09a90"/><stop offset=".5" stop-color="#5d6470"/><stop offset="1" stop-color="#3a3d46"/></linearGradient>
      <linearGradient id="front1" x1="0" y1="0" x2="0" y2="1"><stop offset="0" stop-color="#7d9cd4"/><stop offset=".45" stop-color="#c9ced8"/><stop offset=".75" stop-color="#9aa3b0"/><stop offset="1" stop-color="#55585f"/></linearGradient>
      <linearGradient id="panel1" x1="0" y1="0" x2="0" y2="1"><stop offset="0" stop-color="#e6e5ee"/><stop offset="1" stop-color="#c9c7d9"/></linearGradient>
    </defs>
    <rect role="img" aria-label="Photo of a mall atrium with suspended rectangular light fixtures and a potted palm" width="348" height="848" fill="url(#atrium1)"/>
    <polygon role="img" aria-label="Photo of a retail store interior with a pendant fixture" points="160,0 348,0 348,190" fill="url(#store1)"/>
    <line x1="160" y1="0" x2="348" y2="190" stroke="var(--gap)" stroke-width="6"/>
    <polygon role="img" aria-label="Photo of a supermarket storefront at dusk" points="348,580 348,848 80,848" fill="url(#front1)"/>
    <polygon points="0,232 348,565 80,848 0,848" fill="url(#panel1)"/>
    <polygon points="0,330 240,565 20,790 0,790" fill="var(--lavender-light)" opacity=".55"/>
    <line x1="0" y1="232" x2="348" y2="565" stroke="var(--gap)" stroke-width="7"/>
    <line x1="348" y1="582" x2="82" y2="848" stroke="var(--gap)" stroke-width="7"/>
  </svg>
  <div class="offer">
    <p class="offer__title">Your Design Vision Realized:</p>
    <ul class="offer__list">
      <li>- In-house Design and Custom Capability</li>
      <li>- Engineered and Produced in the United States</li>
      <li>- Elegant, architectural lines incorporating LED, Fluorescent, Halogen and CMH</li>
      <li>- Quick Turnaround from Concept to Production</li>
    </ul>
  </div>
  <ul class="contact">
    <li class="contact__item"><svg class="contact__icon" viewBox="0 0 24 20"><rect x="1" y="3" width="22" height="14" fill="var(--brand-red)"/><polyline points="1,3 12,12 23,3" fill="none" stroke="#fff" stroke-width="1.5"/></svg>dana@kvrlighting.com</li>
    <li class="contact__item"><svg class="contact__icon" viewBox="0 0 24 20"><rect x="7" y="0.5" width="10" height="19" rx="2" fill="none" stroke="var(--brand-red)" stroke-width="1.6"/><circle cx="12" cy="16.5" r="1" fill="var(--brand-red)"/></svg>(555) 410.2873</li>
    <li class="contact__item"><svg class="contact__icon" viewBox="0 0 24 20"><circle cx="12" cy="10" r="9" fill="none" stroke="var(--brand-red)" stroke-width="1.6"/><ellipse cx="12" cy="10" rx="4" ry="9" fill="none" stroke="var(--brand-red)" stroke-width="1.2"/><line x1="3" y1="10" x2="21" y2="10" stroke="var(--brand-red)" stroke-width="1.2"/></svg>www.kvrlighting.com</li>
  </ul>
</section>

<section class="banner banner--two">
  <header class="banner__header">
    <div class="brand"><span class="brand__square"></span><span class="brand__name">KVR</span></div>
    <div class="brand__division">NATIONAL ACCOUNTS</div>
    <div class="brand__tagline">PARTNERSHIP AT EVERY LEVEL</div>
  </header>
  <svg class="banner__art" viewBox="0 0 348 848">
    <defs>
      <linearGradient id="atrium2" x1="0" y1="0" x2="1" y2="1"><stop offset="0" stop-color="#f5eddd"/><stop offset=".3" stop-color="#ecdcbb"/><stop offset=".5" stop-color="#c9b792"/><stop offset=".65" stop-color="#717756"/><stop offset=".85" stop-color="#4e4a37"/><stop offset="1" stop-color="#3a3226"/></linearGradient>
      <linearGradient id="store2" x1="0" y1="0" x2="1" y2="1"><stop offset="0" stop-color="#a09a90"/><stop offset=".5" stop-color="#5d6470"/><stop offset="1" stop-color="#3a3d46"/></linearGradient>
      <linearGradient id="hall2" x1="0" y1="0" x2="0" y2="1"><stop offset="0" stop-color="#f4f1e8"/><stop offset=".5" stop-color="#d9d5ca"/><stop offset="1" stop-color="#8f8c82"/></linearGradient>
      <linearGradient id="panel2" x1="0" y1="0" x2="0" y2="1"><stop offset="0" stop-color="#e6e5ee"/><stop offset="1" stop-color="#c9c7d9"/></linearGradient>
    </defs>
    <rect role="img" aria-label="Photo of a mall atrium with suspended rectangular light fixtures and a potted palm" width="348" height="848" fill="url(#atrium2)"/>
    <polygon role="img" aria-label="Photo of a retail store interior with a pendant fixture" points="160,0 348,0 348,190" fill="url(#store2)"/>
    <line x1="160" y1="0" x2="348" y2="190" stroke="var(--gap)" stroke-width="6"/>
    <polygon role="img" aria-label="Photo of a bright atrium with hanging light columns above an escalator" points="348,580 348,848 80,848" fill="url(#hall2)"/>
    <polygon points="0,232 348,565 80,848 0,848" fill="url(#panel2)"/>
    <polygon points="0,330 240,565 20,790 0,790" fill="var(--lavender-light)" opacity=".55"/>
    <line x1="0" y1="232" x2="348" y2="565" stroke="var(--gap)" stroke-width="7"/>
    <line x1="348" y1="582" x2="82" y2="848" stroke="var(--gap)" stroke-width="7"/>
  </svg>
  <div class="offer">
    <p class="offer__title">Your Design Vision Realized:</p>
    <ul class="offer__list">
      <li>- In-house Design and Custom Capability</li>
      <li>- Engineered and Produced in the United States</li>
      <li>- Elegant, architectural lines incorporating LED, Fluorescent, Halogen and CMH</li>
      <li>- Quick Turnaround from Concept to Production</li>
    </ul>
  </div>
  <ul class="contact">
    <li class="contact__item"><svg class="contact__icon" viewBox="0 0 24 20"><rect x="1" y="3" width="22" height="14" fill="var(--brand-red)"/><polyline points="1,3 12,12 23,3" fill="none" stroke="#fff" stroke-width="1.5"/></svg>dana@kvrlighting.com</li>
    <li class="contact__item"><svg class="contact__icon" viewBox="0 0 24 20"><rect x="7" y="0.5" width="10" height="19" rx="2" fill="none" stroke="var(--brand-red)" stroke-width="1.6"/><circle cx="12" cy="16.5" r="1" fill="var(--brand-red)"/></svg>(555) 410.2873</li>
    <li class="contact__item"><svg class="contact__icon" viewBox="0 0 24 20"><circle cx="12" cy="10" r="9" fill="none" stroke="var(--brand-red)" stroke-width="1.6"/><ellipse cx="12" cy="10" rx="4" ry="9" fill="none" stroke="var(--brand-red)" stroke-width="1.2"/><line x1="3" y1="10" x2="21" y2="10" stroke="var(--brand-red)" stroke-width="1.2"/></svg>www.kvrlighting.com</li>
  </ul>
</section>

<section class="banner banner--three">
  <header class="banner__header">
    <div class="brand"><span class="brand__square"></span><span class="brand__name">KVR</span></div>
    <div class="brand__division">NATIONAL ACCOUNTS</div>
    <div class="brand__tagline">PARTNERSHIP AT EVERY LEVEL</div>
  </header>
  <svg class="banner__art" viewBox="0 0 348 848">
    <defs>
      <linearGradient id="atrium3" x1="0" y1="0" x2="1" y2="1"><stop offset="0" stop-color="#f5eddd"/><stop offset=".3" stop-color="#ecdcbb"/><stop offset=".5" stop-color="#c9b792"/><stop offset=".65" stop-color="#717756"/><stop offset=".85" stop-color="#4e4a37"/><stop offset="1" stop-color="#3a3226"/></linearGradient>
      <linearGradient id="store3" x1="0" y1="0" x2="1" y2="1"><stop offset="0" stop-color="#f1f2f5"/><stop offset=".6" stop-color="#d2d5dc"/><stop offset="1" stop-color="#b4a69a"/></linearGradient>
      <linearGradient id="luggage3" x1="0" y1="0" x2="0" y2="1"><stop offset="0" stop-color="#cfc5b6"/><stop offset=".5" stop-color="#8a6c52"/><stop offset="1" stop-color="#4a3628"/></linearGradient>
      <linearGradient id="panel3" x1="0" y1="0" x2="0" y2="1"><stop offset="0" stop-color="#e6e5ee"/><stop offset="1" stop-color="#c9c7d9"/></linearGradient>
    </defs>
    <rect role="img" aria-label="Photo of a mall atrium with suspended rectangular light fixtures and a potted palm" width="348" height="848" fill="url(#atrium3)"/>
    <polygon role="img" aria-label="Photo of a bright electronics store with recessed ceiling lights" points="160,0 348,0 348,190" fill="url(#store3)"/>
    <line x1="160" y1="0" x2="348" y2="190" stroke="var(--gap)" stroke-width="6"/>
    <polygon role="img" aria-label="Photo of a luggage store interior with display tables" points="348,580 348,848 80,848" fill="url(#luggage3)"/>
    <polygon points="0,232 348,565 80,848 0,848" fill="url(#panel3)"/>
    <polygon points="0,330 240,565 20,790 0,790" fill="var(--lavender-light)" opacity=".55"/>
    <line x1="0" y1="232" x2="348" y2="565" stroke="var(--gap)" stroke-width="7"/>
    <line x1="348" y1="582" x2="82" y2="848" stroke="var(--gap)" stroke-width="7"/>
  </svg>
  <div class="offer">
    <p class="offer__title">Your Design Vision Realized:</p>
    <ul class="offer__list">
      <li>- In-house Design and Custom Capability</li>
      <li>- Engineered and Produced in the United States</li>
      <li>- Elegant, architectural lines incorporating LED, Fluorescent, Halogen and CMH</li>
      <li>- Quick Turnaround from Concept to Production</li>
    </ul>
  </div>
  <ul class="contact">
    <li class="contact__item"><svg class="contact__icon" viewBox="0 0 24 20"><rect x="1" y="3" width="22" height="14" fill="var(--brand-red)"/><polyline points="1,3 12,12 23,3" fill="none" stroke="#fff" stroke-width="1.5"/></svg>dana@kvrlighting.com</li>
    <li class="contact__item"><svg class="contact__icon" viewBox="0 0 24 20"><rect x="7" y="0.5" width="10" height="19" rx="2" fill="none" stroke="var(--brand-red)" stroke-width="1.6"/><circle cx="12" cy="16.5" r="1" fill="var(--brand-red)"/></svg>(555) 410.2873</li>
    <li class="contact__item"><svg class="contact__icon" viewBox="0 0 24 20"><circle cx="12" cy="10" r="9" fill="none" stroke="var(--brand-red)" stroke-width="1.6"/><ellipse cx="12" cy="10" rx="4" ry="9" fill="none" stroke="var(--brand-red)" stroke-width="1.2"/><line x1="3" y1="10" x2="21" y2="10" stroke="var(--brand-red)" stroke-width="1.2"/></svg>www.kvrlighting.com</li>
  </ul>
</section>

</body>
</html>
```